New Business Card Design Project

We would like a business card that represents the sale of boat, home, auto, and life insurance.

The logo can change colors to meet the look of the design if needed.

Industry/Entity Type

Business

```html
<!DOCTYPE html>
<html lang="en">
<head>
<meta charset="utf-8">
<title>Nova Harbor – Business Card</title>
<link href="https://fonts.googleapis.com/css2?family=Questrial&display=swap" rel="stylesheet">
<style>
  :root {
    --stage: #2b2b2b;
    --card-white: #ffffff;
    --card-dark: #2e2e2e;
    --pattern-dark: #353535;
    --brand-green: #7b9b2f;
    --brand-grey: #4a4a4a;
    --text-grey: #555555;
    --band-grey: #3a3a3a;
  }
  * { margin: 0; padding: 0; box-sizing: border-box; }
  html, body {
    width: 1200px; height: 1000px; overflow: hidden;
    background: var(--stage);
    font-family: "Questrial", sans-serif;
  }
  .canvas { position: relative; width: 1200px; height: 1000px; }

  .card {
    position: absolute; width: 560px; height: 320px;
    border-radius: 16px; overflow: hidden;
  }
  .card-front { left: 30px; top: 340px; background: var(--card-white); }
  .card-back { left: 610px; top: 340px; background: var(--card-dark); }

  /* front: contact column */
  .person-name {
    position: absolute; left: 40px; top: 112px;
    font-size: 26px; font-weight: 400; color: var(--brand-green); letter-spacing: 0.3px;
  }
  .person-title {
    position: absolute; left: 42px; top: 146px;
    font-size: 14px; color: var(--text-grey);
  }
  .contact-list {
    position: absolute; left: 42px; top: 176px; list-style: none;
  }
  .contact-list li {
    display: flex; align-items: center; gap: 8px;
    font-size: 13px; color: var(--text-grey); height: 19px;
  }
  .contact-list svg { width: 11px; height: 11px; flex: none; }
  .address {
    position: absolute; left: 300px; top: 176px;
    font-size: 13px; line-height: 19px; color: var(--text-grey);
    font-style: normal;
  }

  /* front: brand block */
  .brand-block {
    position: absolute; right: 40px; top: 40px; text-align: right;
  }
  .brand-name {
    display: flex; align-items: center; justify-content: flex-end; gap: 12px;
    font-size: 28px; letter-spacing: 5px; color: var(--brand-grey);
  }
  .brand-dot {
    width: 16px; height: 16px; border-radius: 50%; background: var(--brand-green);
  }
  .brand-tagline {
    margin-top: 8px; font-size: 14px; letter-spacing: 1px; color: #333333;
  }

  /* front: bottom bands */
  .accent-line {
    position: absolute; left: 0; right: 0; top: 280px; height: 3px;
    background: var(--brand-green);
  }
  .base-band {
    position: absolute; left: 0; right: 0; top: 292px; bottom: 0;
    background: var(--band-grey);
  }

  /* back */
  .back-pattern {
    position: absolute; inset: 0;
    background: linear-gradient(135deg, var(--pattern-dark), var(--card-dark));
  }
  .back-mark {
    position: absolute; left: 0; right: 0; top: 146px;
    display: flex; align-items: center; justify-content: center; gap: 10px;
    font-size: 22px; letter-spacing: 4px; color: #8a8a8a;
  }
  .back-mark .brand-dot { width: 14px; height: 14px; }
</style>
</head>
<body>
<main class="canvas">

  <section class="card card-front" aria-label="Business card front">
    <div class="brand-block">
      <div class="brand-name"><span class="brand-dot"></span>NOVA HARBOR</div>
      <p class="brand-tagline">investments &amp; insurance</p>
    </div>

    <h1 class="person-name">Daniel Hart</h1>
    <p class="person-title">General Manager</p>

    <ul class="contact-list">
      <li>
        <svg viewBox="0 0 12 12" aria-hidden="true"><rect x="3" y="0.5" width="6" height="11" rx="1" fill="none" stroke="#7b9b2f" stroke-width="1.2"/></svg>
        555 010 2468
      </li>
      <li>
        <svg viewBox="0 0 12 12" aria-hidden="true"><rect x="0.5" y="2" width="11" height="8" fill="#7b9b2f"/><path d="M0.5 2 L6 7 L11.5 2" fill="none" stroke="#fff" stroke-width="1"/></svg>
        daniel.hart@example.com
      </li>
      <li>
        <svg viewBox="0 0 12 12" aria-hidden="true"><circle cx="6" cy="6" r="5.5" fill="#7b9b2f"/><path d="M0.5 6 H11.5 M6 0.5 V11.5" stroke="#fff" stroke-width="0.9"/></svg>
        www.novaharbor.com
      </li>
    </ul>

    <address class="address">
      Harbor Plaza Suite<br>
      Second Floor, Unit 8 20,<br>
      Riverton, NY 10101
    </address>

    <div class="accent-line"></div>
    <div class="base-band"></div>
  </section>

  <section class="card card-back" aria-label="Business card back">
    <div class="back-pattern" role="img" aria-label="Faint repeating brand pattern across the dark card back"></div>
    <div class="back-mark"><span class="brand-dot"></span>NOVA HARBOR</div>
  </section>

</main>
</body>
</html>
```